Dishwashing salt packaging label

We need a packaging label design for dishwasher salt. The product prevents lime, calcium and other mineral buildups in dishwashers as well as softening the water for the best washing results possible.

The brand name is Morvada.

As part of the design a logo and colour scheme/theme are required.
Updates

Target Market(s)

25-55 year olds

Industry/Entity Type

Product

Requirements
Must have
• The packaging is in the form of a pail. The design should be in the form of labels that are stuck on to the area below the flange. The design should also be provided in a format that allows a printer to manipulate the images for printing.

The pail dimensions are shown in the attached pail_specification.pdf file. The pail size is the 2 litre size. An image of the pail is shown in the attached Pail_Image.jpeg file.

Not shown in the pdf document are the following dimensions:

Height from base to flange: 126mm
Diameter directly below the flange: 150mm

The label should have the following information on it:

Australian Owned and Manufactured
www.morvada.com.au
57 Hollow St, Carden Ridge, Queensland, Australia

I would also like to be provided with images of the logo design and elements of the label design separately.

Nice to have
• If you consider that any slogan or other wording is necessary or desirable on the packaging, suggestions are welcome.

The design should look modern and clean.

```html
<!DOCTYPE html>
<html lang="en">
<head>
<meta charset="utf-8">
<title>Morvada dishwasher salt label</title>
<link rel="stylesheet" href="https://fonts.googleapis.com/css2?family=Michroma&family=Syncopate:wght@700&family=Jura:wght@500&family=Arimo:wght@700&display=swap">
<style>
  :root {
    --sky: #a8bce6;
    --stripe: #8ea7dc;
    --shield: #ffffff;
    --tint-soft: #e4eaf5;
    --tint-deep: #c9d4ea;
    --brand-blue: #3a63b4;
    --copy-blue: #4c7fe0;
    --address-blue: #3c5ea8;
    --rule: #2b2b2b;
  }
  html, body {
    margin: 0;
    padding: 0;
    overflow: hidden;
  }
  .label {
    position: relative;
    width: 1200px;
    height: 1000px;
    overflow: hidden;
    background:
      radial-gradient(ellipse 520px 300px at 600px 1000px, rgba(235,240,250,0.85), rgba(235,240,250,0) 100%),
      repeating-linear-gradient(to bottom, var(--sky) 0 14px, var(--stripe) 14px 15px),
      var(--sky);
  }
  .shield {
    position: absolute;
    inset: 0;
    filter: drop-shadow(0 0 8px rgba(40,60,110,0.45));
  }
  .content {
    position: absolute;
    inset: 0;
    text-align: center;
  }
  .brand-name {
    position: absolute;
    top: 82px;
    left: 0;
    width: 1200px;
    margin: 0;
    font-family: "Michroma", sans-serif;
    font-weight: 400;
    font-size: 116px;
    line-height: 1;
    color: var(--brand-blue);
  }
  .product-line {
    position: absolute;
    top: 222px;
    left: 0;
    width: 1200px;
    margin: 0;
    font-family: "Syncopate", sans-serif;
    font-weight: 700;
    font-size: 24px;
    letter-spacing: 6px;
    color: var(--brand-blue);
  }
  .rule {
    position: absolute;
    left: 409px;
    width: 393px;
    height: 2px;
    background: var(--rule);
  }
  .rule--one { top: 326px; }
  .rule--two { top: 489px; }
  .rule--three { top: 627px; }
  .claim {
    position: absolute;
    left: 0;
    width: 1200px;
    margin: 0;
    font-family: "Arimo", Arial, sans-serif;
    font-weight: 700;
    font-size: 24px;
    color: var(--copy-blue);
    text-shadow: 0 1px 1px rgba(20,40,90,0.55);
  }
  .claim--benefit { top: 395px; left: 6px; letter-spacing: 1.9px; }
  .claim--origin { top: 546px; letter-spacing: 1.3px; }
  .website {
    position: absolute;
    top: 680px;
    left: 6px;
    width: 1200px;
    margin: 0;
    font-family: "Arimo", Arial, sans-serif;
    font-weight: 700;
    font-size: 20px;
    letter-spacing: 0.7px;
    color: var(--copy-blue);
    text-shadow: 0 1px 1px rgba(20,40,90,0.55);
  }
  .address {
    position: absolute;
    top: 756px;
    left: 0;
    width: 1210px;
    margin: 0;
    font-family: "Jura", sans-serif;
    font-weight: 500;
    font-style: normal;
    font-size: 22px;
    line-height: 30px;
    letter-spacing: 3px;
    font-variant: small-caps;
    color: var(--address-blue);
  }
</style>
</head>
<body>
<div class="label">
  <svg class="shield" width="1200" height="1000" viewBox="0 0 1200 1000">
    <defs>
      <radialGradient id="shield-tone" cx="50%" cy="50%" r="62%">
        <stop offset="0%" stop-color="#ffffff"/>
        <stop offset="45%" stop-color="#ffffff"/>
        <stop offset="80%" stop-color="var(--tint-soft)"/>
        <stop offset="100%" stop-color="var(--tint-deep)"/>
      </radialGradient>
    </defs>
    <path d="M145 0 H1065 V380 C1065 700 800 870 605 972 C410 870 145 700 145 380 Z" fill="var(--shield)"/>
    <path class="shield-decoration" role="img" aria-label="Soft pale blue decorative artwork behind the label text"
          d="M160 0 H1050 V380 C1050 690 795 855 605 952 C415 855 160 690 160 380 Z"
          fill="url(#shield-tone)"/>
  </svg>

  <div class="content">
    <h1 class="brand-name">Morvada</h1>
    <p class="product-line">FOR DISHWASHERS</p>

    <div class="rule rule--one"></div>
    <p class="claim claim--benefit">Prevents Lime, Calcium and other mineral buildups</p>
    <div class="rule rule--two"></div>
    <p class="claim claim--origin">Australian Owned and Manufactured</p>
    <div class="rule rule--three"></div>

    <p class="website">www.morvada.com.au</p>
    <address class="address">57 Hollow St<br>Carden Ridge<br>Queensland<br>Australia</address>
  </div>
</div>
</body>
</html>
```